New Coffee Shop business card

We are opening our new coffee shop and are needing business cards to take with us on February 6th to Atlanta, Ga to a show.

We will be offering the following menu type items:

coffee
teas
espresso
frappes
smoothies

sandwiches
soups
salads
pastries
ice cream

Our shop is in a rural country-side area and we would like to convey that feel in our shop. In addition to the cafe we will also be selling gifts and furniture and other home decor. Much of this merchandise will be rescued, refurbished or repurposed which is also a core value of what we are all about.

We have a company logo we would like incorporated into the design.

We will also provide files that have the elements of the logo which may also be useful in the design of the card.

Since we are not open yet we need one slightly altered version of the card as well as the final product which states "Opening in the summer 2015"

Target Market(s)

moderate to slightly upscale and folksy.

Industry/Entity Type

Coffee Shop

Contact Information for Business Card

Fern Hollow Coffee
name
address
phone number
email

Card

Font styles to use
Sans Serif

Requirements
Must have
• Must include Logo
• Must include information on menu.
• Must include information on our merchandise sales as described inthe project description.
• Color scheme to complement the logo
Nice to have
• The following descriptions
• "We are also selling gifts, furniture, and other home decoration."
• "We rescue, refurbish, and repurpose old furniture so it can live again."

```html
<!DOCTYPE html>
<html lang="en">
<head>
<meta charset="utf-8">
<title>Fern Hollow Coffee – Business Cards</title>
<link href="https://fonts.googleapis.com/css2?family=Jost:ital,wght@0,300;0,400;0,600;0,700;1,600&display=swap" rel="stylesheet">
<style>
  :root {
    --page: #e9e5df;
    --red: #b8354a;
    --red-deep: #8c1e32;
    --red-light: #cf4a5e;
    --ink: #111111;
    --ink-soft: #2b2b2b;
    --paper: #f7f5f3;
    --cream: #ecdcc6;
    --white: #ffffff;
  }
  * { box-sizing: border-box; margin: 0; padding: 0; }
  html, body {
    width: 1200px; height: 1000px; overflow: hidden;
    background: var(--page);
    font-family: "Jost", sans-serif;
  }
  .card {
    position: absolute;
    width: 600px; height: 343px;
    overflow: hidden;
    box-shadow: 0 10px 24px rgba(0,0,0,.25);
  }

  /* ---------- Front card ---------- */
  .card--front { left: 70px; top: 80px; background: linear-gradient(135deg, var(--red-light), var(--red) 45%, var(--red-deep)); }
  .front__brand-panel {
    position: absolute; left: 0; top: 0; width: 232px; height: 100%;
    background: linear-gradient(160deg, var(--ink-soft), var(--ink));
  }
  .brand-lockup {
    position: absolute; left: 28px; top: 70px;
    display: flex; align-items: center; gap: 12px;
    color: var(--white);
  }
  .brand-lockup__dot { width: 22px; height: 22px; border-radius: 50%; background: var(--white); flex: none; }
  .brand-lockup__name { font-weight: 300; font-size: 30px; line-height: 1.05; }
  .front__bird {
    position: absolute; left: 40px; bottom: 70px; width: 38px; height: 22px;
    border-radius: 50%; background: rgba(255,255,255,.85);
  }
  .front__dog {
    position: absolute; left: 108px; bottom: 18px; width: 104px; height: 110px;
    border-radius: 40% 50% 20% 20%; background: rgba(255,255,255,.9);
  }
  .front__details { position: absolute; left: 262px; top: 26px; width: 290px; color: var(--white); }
  .front__title { font-weight: 300; font-size: 24px; letter-spacing: .5px; }
  .front__names { margin-top: 12px; font-weight: 700; font-size: 22px; line-height: 1.15; color: var(--cream); }
  .front__rule { position: relative; margin-top: 10px; width: 240px; border-top: 2px solid var(--white); }
  .front__role { position: absolute; right: -58px; top: -10px; font-size: 13px; font-weight: 400; }
  .front__address, .front__phones, .front__emails { font-size: 14px; font-weight: 300; line-height: 1.35; }
  .front__address { margin-top: 16px; }
  .front__phones { margin-top: 10px; }
  .front__emails { margin-top: 14px; }
  .front__cup { position: absolute; right: 26px; top: 26px; width: 60px; height: 48px; }
  .front__pointer {
    position: absolute; right: 14px; top: 150px; width: 96px; height: 64px;
    border-radius: 45% 40% 30% 30%; background: rgba(255,255,255,.85);
  }

  /* ---------- Back card ---------- */
  .card--back { left: 540px; top: 570px; background: var(--paper); }
  .back__band {
    position: absolute; inset: 0;
    background: linear-gradient(160deg, var(--red), var(--red-deep));
    clip-path: polygon(0 0, 210px 0, 270px 100%, 0 100%);
  }
  .back__flourish {
    position: absolute; width: 70px; height: 56px; border-radius: 50%;
    background: rgba(184,53,74,.35);
  }
  .back__flourish--top { left: 190px; top: -10px; background: rgba(255,255,255,.45); }
  .back__flourish--bottom { left: 250px; bottom: 10px; }
  .back__quote {
    position: absolute; left: 18px; top: 78px; width: 200px;
    color: var(--white); font-size: 12px; font-weight: 600; line-height: 1.4;
  }
  .back__quote em { font-style: italic; }
  .back__signoff { display: block; margin-top: 8px; font-weight: 700; font-size: 13px; }
  .back__mini-brand {
    position: absolute; left: 296px; top: 20px;
    display: flex; align-items: center; gap: 8px;
    font-size: 15px; font-weight: 400; color: var(--ink-soft);
  }
  .back__mini-brand span:first-child { width: 14px; height: 14px; border-radius: 50%; background: var(--ink-soft); }
  .back__heading { position: absolute; left: 296px; top: 54px; color: var(--red); }
  .back__heading h2 { font-size: 36px; font-weight: 700; line-height: 1; }
  .back__heading p { font-size: 15px; font-weight: 400; color: var(--red-deep); margin-top: 2px; }
  .menu {
    position: absolute; left: 288px; top: 128px; width: 214px; padding: 10px;
    border: 1px solid var(--red); outline: 1px solid var(--red); outline-offset: 3px;
    display: grid; grid-template-columns: auto auto auto; justify-content: space-between;
    column-gap: 8px; row-gap: 2px;
    list-style: none; font-size: 13px; font-weight: 300; color: var(--red);
  }
  .back__opening {
    position: absolute; right: 14px; top: 214px; width: 68px; text-align: center;
    font-size: 17px; font-weight: 700; line-height: 1.15; color: var(--red);
  }
</style>
</head>
<body>

<section class="card card--front" aria-label="Business card, front">
  <div class="front__brand-panel">
    <div class="brand-lockup">
      <span class="brand-lockup__dot"></span>
      <span class="brand-lockup__name">Fern Hollow<br>Coffee</span>
    </div>
    <div class="front__bird" role="img" aria-label="Silhouette of a bird in flight"></div>
    <div class="front__dog" role="img" aria-label="Silhouette of a sitting hunting dog"></div>
  </div>

  <div class="front__details">
    <p class="front__title">The Head Growers</p>
    <p class="front__names">Dale and Marnie<br>Pruett</p>
    <div class="front__rule"><span class="front__role">owners</span></div>
    <p class="front__address">PO Box 42,<br>215 East Mill Street,<br>Ashby, KY 40512</p>
    <p class="front__phones">D: 555-014-2271<br>M: 555-014-6093</p>
    <p class="front__emails">dale@fernhollowcoffee.com<br>marnie@fernhollowcoffee.com</p>
  </div>

  <svg class="front__cup" viewBox="0 0 60 48" aria-hidden="true">
    <path d="M8 12 H44 V24 A18 18 0 0 1 8 24 Z" fill="var(--white)"/>
    <path d="M44 15 A7 7 0 0 1 44 29" fill="none" stroke="var(--white)" stroke-width="4"/>
    <rect x="0" y="42" width="54" height="4" rx="2" fill="var(--white)"/>
  </svg>
  <div class="front__pointer" role="img" aria-label="Silhouette of a pointing dog"></div>
</section>

<section class="card card--back" aria-label="Business card, back">
  <div class="back__band"></div>
  <div class="back__flourish back__flourish--top" role="img" aria-label="Decorative flourish"></div>
  <div class="back__flourish back__flourish--bottom" role="img" aria-label="Decorative flourish"></div>

  <p class="back__quote">“Come on in to visit, eat, or peruse through our <em>“stuff we’re sellin’.”</em> An eclectic assemblage of furnishings, gifts, and home décor. We rescue, refurbish and repurpose old stuff so it can live again.”
    <span class="back__signoff">Hope to see you soon!</span></p>

  <div class="back__mini-brand"><span></span><span>Fern Hollow</span></div>
  <div class="back__heading">
    <h2>Fern Hollow</h2>
    <p>not just a coffee shop…</p>
  </div>

  <ul class="menu">
    <li>coffee</li><li>frappes</li><li>salads</li>
    <li>teas</li><li>smoothies</li><li>pastries</li>
    <li>espresso</li><li>sandwiches</li><li>ice cream</li>
    <li></li><li>soups</li><li></li>
  </ul>

  <p class="back__opening">Opening in the summer 2015</p>
</section>

</body>
</html>
```